Furniture Design Website Homepage

Brief as attached- Homepage Design

Silver Heron Furniture is a national retail emporium offering high quality, unique Scandinavian furniture, lighting and accessories. We are the market leader in this space and currently have 2 Showrooms – Melbourne & Sydney.

Most recently our business model has evolved from purely importing premium, one off vintage pieces to a more scalable model of representing brands and manufacturers exclusively out of Scandinavia. These partners manufacture today which ensures us of supply & quality.

We have now started to engage scandinavian designers and/or their families to re-introduce designs that have long gone out of production. These items are put back into production under the silver heron brand, and we own the world wide rights to them.

Please ensure you use the brief files attached and the catalogue images when creating the design.

Target Market(s)

Silver Heron Furniture - where beautiful Scandinavian design meets my modern Australian life.

We want our target audience to chose Scandinavian for their homes & for us to be their brand of choice.

The current perception is that we offer beautiful design but that it doesn’t suit everyone’s home / life / style.

Also that we are more expensive than most.

Industry/Entity Type

Retail

Requirements
Must have
• The colour scheme should be red and white as per the catalogue I attached. We like the look and feel of this site www.roomwhimsy.example

The furniture is more luxurious, so we need to target the upper market with a nice sleek look that makes the furniture look expensive.

```html
<!DOCTYPE html>
<html lang="en">
<head>
<meta charset="utf-8">
<title>Silver Heron Furniture – Home</title>
<link rel="stylesheet" href="https://fonts.googleapis.com/css2?family=Questrial&family=Didact+Gothic&display=swap">
<style>
:root{
  --red:#c40a0a;
  --red-dark:#8f0303;
  --wood:#9a4a12;
  --wood-light:#b8641f;
  --blue:#1d4fa8;
  --green:#1f7a14;
  --ink:#222;
  --muted:#555;
  --panel:#ebebeb;
  --line:#c9c9c9;
  --white:#fff;
}
*{box-sizing:border-box;margin:0;padding:0}
html,body{width:1200px;height:1181px;overflow:hidden}
body{font-family:"Didact Gothic",sans-serif;color:var(--ink);font-size:11px;background:#cfcfcb}
.canvas{position:relative;width:1200px;height:1181px;overflow:hidden;background:linear-gradient(#d6d6d3,#c7c7c3)}
.abs{position:absolute}
.hero-photo{left:0;top:0;width:1200px;height:190px;background:linear-gradient(180deg,#ececea 0%,#dcdcda 75%,#c8c8c5 100%)}
.brand{left:189px;top:0;width:194px;height:125px;background:linear-gradient(#d11212,var(--red-dark));box-shadow:0 2px 4px rgba(0,0,0,.35);display:flex;align-items:flex-end;justify-content:center;padding-bottom:16px}
.brand span{font-family:"Questrial",sans-serif;color:var(--white);font-size:22px;line-height:1.05;text-align:center}
.tagline{left:392px;top:8px;font-family:"Questrial",sans-serif;color:var(--red);font-size:16px;line-height:19px}
.account{left:930px;top:4px;font-size:11px;color:#222}
.cart{left:892px;top:23px;width:171px;height:160px;background:linear-gradient(160deg,var(--wood-light),var(--wood));border:3px solid #fff;box-shadow:0 1px 4px rgba(0,0,0,.35);color:#fff;font-size:11px}
.cart h3{font-family:"Questrial",sans-serif;font-weight:400;font-size:17px;position:absolute;left:36px;top:7px}
.cart .ln{position:absolute;left:6px}
.cart .view{text-decoration:underline;font-size:9px}
.cart .checkout{position:absolute;left:97px;top:71px;width:67px;height:20px;border-radius:4px;background:linear-gradient(#fff,#d8d8d8);color:#333;font-size:9px;text-align:center;line-height:20px}
.cart .secure{position:absolute;left:50px;top:110px;font-family:"Questrial",sans-serif;font-size:16px;line-height:17px}
.nav{left:200px;top:195px;width:866px;height:39px;background:linear-gradient(#fff,#e9e9e9);display:flex;align-items:center;border-bottom:1px solid var(--line)}
.nav .home{width:62px;display:flex;justify-content:center}
.nav a{font-family:"Questrial",sans-serif;font-size:14.5px;color:#222;text-decoration:none;border-left:1px solid var(--line);height:39px;line-height:39px;text-align:center}
.sidebar{left:198px;top:234px;width:168px;height:830px;background:#fff}
.main{left:368px;top:234px;width:698px;height:830px;background:var(--panel)}
.side-tab{left:189px;width:177px;height:25px;background:linear-gradient(var(--wood-light),var(--wood));color:#fff;font-family:"Questrial",sans-serif;font-size:14.5px;line-height:25px;padding-left:19px;box-shadow:0 1px 2px rgba(0,0,0,.3)}
.side-tab::after{content:"";position:absolute;left:0;top:25px;border-top:6px solid #222;border-left:9px solid transparent}
.field{background:#fff;border:1px solid #bbb;border-radius:3px;height:20px}
.search-field{left:209px;top:287px;width:113px;color:#aaa;font-size:10px;padding:3px 8px}
.search-btn{left:330px;top:287px;width:27px;height:21px;border-radius:4px;background:linear-gradient(#f4f4f4,#cfd8e4);border:1px solid #aab;display:flex;align-items:center;justify-content:center}
.range{left:210px;top:358px;list-style:none;font-size:11.5px}
.range li{height:21px;display:flex;align-items:center;gap:6px}
.range i{width:8px;height:8px;background:#4a8fd0;transform:rotate(45deg);border:1px solid #9cc4ea}
.filter{left:210px;font-size:11.5px;width:148px;height:21px;display:flex;align-items:center;justify-content:space-between}
.select{width:68px;height:15px;border:1px solid #999;background:#fff;position:relative}
.select::after{content:"";position:absolute;right:0;top:0;width:13px;height:13px;background:#eee;border-left:1px solid #999}
.select::before{content:"";position:absolute;right:3px;top:4px;border-top:5px solid #222;border-left:4px solid transparent;border-right:4px solid transparent;z-index:1}
.btn-grey{border:1px solid #999;border-radius:3px;background:linear-gradient(#fff,#dcdcdc);text-align:center;font-size:12px;color:#222}
.side-text{left:209px;top:666px;width:150px;font-size:11px;line-height:16px}
.link{color:var(--blue);text-decoration:underline}
.testimonial{left:209px;top:778px;width:147px;height:169px;background:#fff;border:1px solid #bbb;border-radius:3px;box-shadow:0 1px 3px rgba(0,0,0,.2)}
.testimonial h4{font-family:"Questrial",sans-serif;font-weight:400;font-size:15px;padding:4px 8px;height:27px;background:linear-gradient(#fff,#e6e6e6);border-bottom:1px solid #ccc}
.portrait{position:absolute;left:7px;top:42px;width:50px;height:55px;background:linear-gradient(#dfe6ee,#9aa6b4);border:1px solid #aaa}
.quote-mark{position:absolute;left:68px;top:34px;font-family:"Questrial",sans-serif;font-size:26px;color:#bbb;line-height:1}
.testimonial p{position:absolute;font-size:10.5px;line-height:13px}
.cards{left:209px;top:996px;width:143px;height:50px;border:1px solid #aab;border-radius:3px;background:#fff;display:flex;flex-wrap:wrap;gap:4px;padding:5px 6px;align-content:flex-start}
.cards .wide{width:60px;height:14px;background:#7f95b7;border-radius:6px;margin-left:34px}
.cards .card{width:27px;height:17px;border-radius:2px}
h1.heading{left:383px;top:252px;font-family:"Questrial",sans-serif;font-weight:400;font-size:17px;color:var(--red)}
.intro{left:383px;top:282px;width:652px;font-size:11.5px;line-height:16px}
.feature{left:382px;top:330px;width:666px;height:274px;background:#fff;border:2px solid #fff;box-shadow:0 0 2px rgba(0,0,0,.3)}
.feature-photo{left:386px;top:333px;width:445px;height:270px;background:linear-gradient(135deg,#f2f2f0,#d9d9d6 60%,#eeeeec)}
.cat{left:840px;width:200px;height:78px;background:#fff;box-shadow:0 1px 3px rgba(0,0,0,.25)}
.cat .thumb{position:absolute;left:0;top:0;width:75px;height:78px}
.cat h3{position:absolute;left:88px;top:20px;font-family:"Questrial",sans-serif;font-weight:400;font-size:18px;color:var(--blue)}
.cat span{position:absolute;left:88px;top:45px;font-size:11.5px}
.products{left:382px;top:623px;width:665px;height:317px;background:linear-gradient(#fff 20%,#fbd9d9);box-shadow:0 0 3px rgba(0,0,0,.2)}
.products-title{left:434px;top:627px;font-family:"Questrial",sans-serif;font-size:17px;color:var(--red)}
.product{top:659px;width:152px;height:268px;background:#fff;border:1px solid #ccc;border-radius:3px;box-shadow:0 1px 4px rgba(0,0,0,.3)}
.product .photo{position:absolute;left:6px;top:10px;width:138px;height:150px;background:linear-gradient(#f6f6f6,#e2e2e2)}
.product .name{position:absolute;left:0;width:100%;top:176px;text-align:center;font-family:"Questrial",sans-serif;font-size:17px;color:var(--blue)}
.product .price{position:absolute;left:0;width:100%;top:202px;text-align:center;font-family:"Questrial",sans-serif;font-size:29px;color:#111}
.product .price b{color:var(--green);font-weight:400}
.product .more{position:absolute;left:6px;top:239px;width:66px;height:22px;line-height:20px;font-size:10px;border-radius:4px}
.product .add{position:absolute;left:80px;top:239px;width:66px;height:22px;line-height:22px;font-size:10px;border-radius:4px;background:linear-gradient(#e01515,var(--red-dark));color:#fff;text-align:center}
.newsletter{left:399px;top:953px;width:629px;height:102px;background:#fff;border:1px solid #bbb;border-radius:3px}
.newsletter .bar{height:27px;background:linear-gradient(#fafafa,#e2e2e2);border-bottom:1px solid #ccc;font-family:"Questrial",sans-serif;font-size:16px;padding:3px 0 0 40px}
.newsletter .lbl{position:absolute;font-size:11.5px}
.newsletter .inp{position:absolute;height:16px;border:1px solid #aaa;background:#fff}
.join-now{left:878px;top:989px;width:141px;height:36px;border-radius:5px;background:linear-gradient(#35a0e8,#0b5fae);color:#fff;font-family:"Questrial",sans-serif;font-size:22px;line-height:36px;padding-left:11px;box-shadow:0 1px 3px rgba(0,0,0,.4)}
.footer{left:0;top:1064px;width:1200px;height:117px;background:linear-gradient(var(--red),#b40000)}
.footer .copy{position:absolute;left:230px;top:10px;color:#fff;font-size:10px;font-weight:700;letter-spacing:.5px}
.footer .mark{position:absolute;left:208px;top:74px;color:#fff;font-family:"Questrial",sans-serif;font-size:21px}
.footer .rights{position:absolute;left:228px;top:101px;color:#fff;font-size:10px;font-weight:700;letter-spacing:.5px}
.fcol{position:absolute;top:20px;color:#fff;font-size:10px}
.fcol h5{font-size:10px;font-weight:700;letter-spacing:.5px;padding-bottom:6px;border-bottom:1px dotted rgba(255,255,255,.6);width:105px;margin-bottom:5px}
.fcol li{list-style:none;line-height:11.5px}
.fcol li::before{content:"› ";font-weight:700}
</style>
</head>
<body>
<div class="canvas">

  <div class="abs hero-photo" role="img" aria-label="Bright living room with a white sofa, armchair with orange throw and floor speaker"></div>
  <div class="abs brand"><span>Silver Heron<br>Furniture</span></div>
  <div class="abs tagline">THE BEST OF MODERN AND<br>CLASSIC SCANDINAVIAN DESIGN</div>
  <div class="abs account">Account/Login | Sign Up</div>

  <div class="abs cart">
    <svg class="abs" style="left:7px;top:8px" width="24" height="20" viewBox="0 0 24 20"><path d="M1 2h4l3 11h12l3-8H7" fill="none" stroke="#fff" stroke-width="2"/><circle cx="10" cy="17" r="2" fill="#fff"/><circle cx="18" cy="17" r="2" fill="#fff"/></svg>
    <h3>Shopping Cart</h3>
    <div class="ln" style="top:43px">Item : 0</div>
    <div class="ln" style="top:64px">Total : $0.00</div>
    <div class="ln view" style="top:97px">View Cart</div>
    <div class="checkout">Check Out</div>
    <svg class="abs" style="left:14px;top:106px" width="32" height="36" viewBox="0 0 32 36"><circle cx="16" cy="18" r="15" fill="#2f9a2a" stroke="#fff" stroke-width="2"/><path d="M9 18l5 5 10-11" fill="none" stroke="#fff" stroke-width="3"/></svg>
    <div class="secure">Secure<br>Shopping</div>
  </div>

  <nav class="abs nav">
    <div class="home"><svg width="28" height="28" viewBox="0 0 28 28"><circle cx="14" cy="14" r="13" fill="var(--red)"/><path d="M7 15l7-6 7 6M9 14v6h10v-6" fill="none" stroke="#222" stroke-width="2"/></svg></div>
    <a style="width:107px">About Us</a>
    <a style="width:99px">Furniture</a>
    <a style="width:107px">Restoration</a>
    <a style="width:76px">Media</a>
    <a style="width:58px">FAQ</a>
    <a style="width:105px">Mailing List</a>
    <a style="width:63px">Blog</a>
    <a style="width:105px">Site Search</a>
    <a style="width:113px">Contact Us</a>
  </nav>

  <aside class="abs sidebar"></aside>
  <main class="abs main"></main>

  <div class="abs side-tab" style="top:252px">Product Search</div>
  <div class="abs field search-field">Search...</div>
  <div class="abs search-btn"><svg width="15" height="15" viewBox="0 0 15 15"><circle cx="6" cy="6" r="4.5" fill="none" stroke="#245" stroke-width="2"/><path d="M9.5 9.5l4 4" stroke="#245" stroke-width="2.5"/></svg></div>

  <div class="abs side-tab" style="top:322px">Browse Our Range</div>
  <ul class="abs range">
    <li><i></i>Furniture</li>
    <li><i></i>Furniture Packages</li>
    <li><i></i>Accessories</li>
    <li><i></i>Lightings</li>
    <li><i></i>Fabrics</li>
  </ul>

  <div class="abs side-tab" style="top:463px">View Product by Type</div>
  <div class="abs filter" style="top:491px">Room:<span class="select"></span></div>
  <div class="abs filter" style="top:512px">Furniture:<span class="select"></span></div>
  <div class="abs filter" style="top:533px">Designers:<span class="select"></span></div>
  <div class="abs filter" style="top:554px">Brands:<span class="select"></span></div>
  <div class="abs filter" style="top:575px">Accessories:<span class="select"></span></div>
  <div class="abs btn-grey" style="left:209px;top:606px;width:140px;height:20px;line-height:18px">Find Product</div>

  <div class="abs side-tab" style="top:640px">Keep Up to Date</div>
  <div class="abs side-text">Discover exclusive offer, products previews and much more.</div>
  <div class="abs btn-grey" style="left:209px;top:721px;width:140px;height:20px;line-height:18px">Join Our Newsletter</div>
  <div class="abs link" style="left:215px;top:748px;font-size:12px">We value Your Privacy</div>

  <section class="abs testimonial">
    <h4>Testimonial</h4>
    <div class="portrait" role="img" aria-label="Customer portrait"></div>
    <div class="quote-mark">“</div>
    <p style="left:64px;top:58px;width:82px">dolor sit amet, consectetuer adipiscing elit. Aeneancommo</p>
    <p style="left:8px;top:110px;width:138px">do ligula eget dolor. Aen eanmassa. Cum sociis n atoque penatibus et ma gnis dis .</p>
    <p style="left:76px;top:154px;font-size:9px;font-weight:700">R.K Holloway</p>
  </section>

  <div class="abs side-tab" style="top:966px">Accepted credit card</div>
  <div class="abs cards">
    <span class="wide"></span>
    <span class="card" style="background:#d9541e"></span>
    <span class="card" style="background:#1f3f95"></span>
    <span class="card" style="background:#3a86c8"></span>
    <span class="card" style="background:#e08a2a"></span>
  </div>

  <h1 class="abs heading">Heading</h1>
  <p class="abs intro">Lorem ipsum dolor sit amet, consectetur adipisicing elit, sed do eiusmod tempor incididunt ut labore et dolore magna aliqua. Ut enim ad minim veniam, quis nostrud exercitation ullamco laboris nisi ut aliquip ex ea commodo consequat.</p>

  <div class="abs feature"></div>
  <div class="abs feature-photo" role="img" aria-label="White Scandinavian living room with sofa, side tables and tall windows"></div>
  <div class="abs cat" style="top:340px"><div class="thumb" role="img" aria-label="Lounge chair collection" style="background:linear-gradient(#ece8e2,#c9a58c 70%,#c5332f)"></div><h3>Furniture</h3><span>View Collection</span></div>
  <div class="abs cat" style="top:429px"><div class="thumb" role="img" aria-label="Patterned cups and vases" style="background:linear-gradient(135deg,#e5ecf4,#5a7fb8 60%,#2a2a2a)"></div><h3>Accessories</h3><span>View Collection</span></div>
  <div class="abs cat" style="top:516px"><div class="thumb" role="img" aria-label="Timber pendant lights" style="background:linear-gradient(90deg,#f3e9d8,#c9a06a 60%,#5a3820)"></div><h3>Lighting</h3><span>View Collection</span></div>

  <div class="abs products"></div>
  <div class="abs products-title">Silver Heron</div>

  <div class="abs product" style="left:401px"><div class="photo" role="img" aria-label="Black leather chaise longue"></div><div class="name">Product Name</div><div class="price"><b>$</b>2.299</div><div class="btn-grey more">More Detail</div><div class="add">Add to Cart</div></div>
  <div class="abs product" style="left:559px"><div class="photo" role="img" aria-label="White layered shade table and floor lamps"></div><div class="name">Product Name</div><div class="price"><b>$</b>2.299</div><div class="btn-grey more">More Detail</div><div class="add">Add to Cart</div></div>
  <div class="abs product" style="left:718px"><div class="photo" role="img" aria-label="Beige tufted wingback armchair"></div><div class="name">Product Name</div><div class="price"><b>$</b>2.299</div><div class="btn-grey more">More Detail</div><div class="add">Add to Cart</div></div>
  <div class="abs product" style="left:877px"><div class="photo" role="img" aria-label="Light blue upholstered lounge chair"></div><div class="name">Product Name</div><div class="price"><b>$</b>2.299</div><div class="btn-grey more">More Detail</div><div class="add">Add to Cart</div></div>

  <section class="abs newsletter">
    <svg class="abs" style="left:10px;top:6px" width="22" height="16" viewBox="0 0 22 16"><rect x="1" y="1" width="20" height="14" fill="#ddd" stroke="#777"/><path d="M1 1l10 8 10-8" fill="none" stroke="#777"/></svg>
    <div class="bar">Join Our Newsletter</div>
    <div class="lbl" style="left:12px;top:37px">Discover exclusive offers, product previews, information on sales and much more!</div>
    <div class="lbl" style="left:20px;top:64px">Name:</div><div class="inp" style="left:60px;top:63px;width:138px"></div>
    <div class="lbl" style="left:20px;top:85px">State:</div><div class="inp" style="left:60px;top:84px;width:94px"><span style="position:absolute;right:0;top:0;width:15px;height:14px;background:#ccc"></span></div>
    <div class="lbl" style="left:249px;top:64px">Email:</div><div class="inp" style="left:288px;top:63px;width:138px"></div>
    <div class="lbl" style="left:216px;top:85px">Postalcode:</div><div class="inp" style="left:288px;top:84px;width:138px"></div>
    <div class="lbl link" style="left:490px;top:84px">We Value Your Privacy</div>
  </section>
  <div class="abs join-now">Join NOW »</div>

  <footer class="abs footer">
    <div class="copy">Copyright © 2011</div>
    <div class="mark">silver heron</div>
    <div class="rights">All Rights Reserved</div>
    <div class="fcol" style="left:411px"><h5>Home:</h5><ul><li>Navigation Link 1</li><li>Navigation Link 2</li><li>Navigation Link 3</li><li>Navigation Link 4</li><li>Navigation Link 5</li></ul></div>
    <div class="fcol" style="left:551px"><h5>Furniture:</h5><ul><li>Navigation Link 1</li><li>Navigation Link 2</li><li>Navigation Link 3</li><li>Navigation Link 4</li><li>Navigation Link 5</li></ul></div>
    <div class="fcol" style="left:689px"><h5>Restoration:</h5><ul><li>Navigation Link 1</li><li>Navigation Link 2</li><li>Navigation Link 3</li><li>Navigation Link 4</li><li>Navigation Link 5</li></ul></div>
    <div class="fcol" style="left:826px"><h5>Media:</h5><ul><li>Navigation Link 1</li><li>Navigation Link 2</li><li>Navigation Link 3</li><li>Navigation Link 4</li><li>Navigation Link 5</li></ul></div>
    <div class="fcol" style="left:957px"><h5>Contact Us:</h5><ul><li>Navigation Link 1</li><li>Navigation Link 2</li><li>Navigation Link 3</li><li>Navigation Link 4</li><li>Navigation Link 5</li></ul></div>
  </footer>

</div>
</body>
</html>
```